International Petrochemical business needs a web design for Clearway Desk system

We need a web design for a "Clearway Desk" system for an international petrochemical company. The web site is used internally within the company. It is hosted by an internal department which provides government permit request service for other departments.

We would like to see designs of two pages using color light blue. (home page, internal page as attached).
Home Page:
1. Header has a background image and small animation. Header on home page can be taller than the header of the internal page.
2. Layout as attached.

Internal Page:
1. Header can use the same background image as the home page and can be shorter to utilize the page for content.
2. The blue icon behind every captions represent an icon. When user move mouse over this icon, it displays the caption in Thai language as a tooltip. This icon needs to be redesign.

The final design should communicate the followings:
- Excellent service provided system in terms of time and accurary
- Rapid growth of business via building petrochemical refinery plant

For Internal Page, the blue circle behind every captions represent an icon. When mouse over this icon, a tool tip showing the caption in Thai language is shown. Please also design this icon..

There are more feedbacks from customer as followed:

1. Banner should consists of 
    1.1 "Approved" stamp on paper
    1.2 An image of Garuda. It is used on every government documents in Thailand
    1.3 Image of petrochemical plant
2. Each menu item (Home, Permit, Search, etc) should have different colors. Drop down menu will use the same color as its parent menu item.
3. Overall tone of the web page should be light blue with background of the body the web page in white
4. "New Request" button should use green color with icon on it
5. Table header of each box in the body of the page should use dark blue background with text in white

Please kindly submit your revisions.
Thank you.

Reason: We get some late feedbacks from customers which was just updated to all designers.

• 1. Design for 1024x768 screen resolution
2. Use light blue theme
3. Background of header where the company logo is must have white background

```html
<!DOCTYPE html>
<html lang="en">
<head>
<meta charset="utf-8">
<title>Northvale Petrochemical Clearway Desk</title>
<link href="https://fonts.googleapis.com/css2?family=Arimo:wght@400;700&display=swap" rel="stylesheet">
<style>
:root{
  --navy:#1c1464;
  --navy-2:#2a1d9a;
  --sky:#0aa3e0;
  --sky-light:#2cbcf2;
  --sky-line:#0b9ad6;
  --frame:#9fd3ee;
  --head-gray:#e0e0e0;
  --row-a:#dcdbea;
  --row-b:#d6eef8;
  --link:#0a8fd1;
  --ink:#111;
  --ink-soft:#333;
}
*{box-sizing:border-box;margin:0;padding:0}
html,body{width:1200px;height:1170px;overflow:hidden;background:#fff}
body{position:relative;font-family:"Arimo",Arial,sans-serif;color:var(--ink)}

.top-rule{position:absolute;left:89px;top:3px;width:1024px;height:3px;background:var(--sky)}

.brand{position:absolute;left:97px;top:18px;display:flex;align-items:center;gap:8px}
.brand-dot{width:38px;height:38px;border-radius:50%;background:var(--sky)}
.brand-name{color:var(--sky-line);font-weight:700;font-size:16px;line-height:18px}

.main-nav{position:absolute;left:441px;top:37px;display:flex;gap:2px}
.nav-tab{width:103px;height:38px;border-radius:6px 6px 0 0;background:var(--navy);color:#fff;font-size:15px;display:flex;align-items:center;justify-content:center;padding-top:4px}
.nav-tab.is-active{background:linear-gradient(#1aa9e6,#0a7fc8)}
.nav-tab.is-open{background:var(--navy)}
.nav-rule{position:absolute;left:89px;top:75px;width:1024px;height:4px;background:var(--navy)}

.dropdown{position:absolute;left:547px;top:80px;width:188px;background:var(--navy);padding:3px 0}
.dropdown a{display:block;height:30.5px;line-height:30px;padding-left:26px;color:var(--sky-light);font-size:14px;text-decoration:none;border-bottom:1px solid #2b2380}
.dropdown a:last-child{border-bottom:0}

.banner{position:absolute;left:89px;top:79px;width:1024px;height:291px;
  background:linear-gradient(180deg,#6f9fd0 0%,#a9c6e3 35%,#d9dfe6 55%,#9ea6ad 75%,#5d6266 100%)}
.banner-base{position:absolute;left:89px;top:370px;width:1024px;height:9px;background:var(--navy)}
.banner-arrow{position:absolute;top:205px;width:37px;height:40px;background:#3b3b3b;display:flex;align-items:center;justify-content:center}
.banner-arrow.prev{left:111px}
.banner-arrow.next{left:1054px}

.panel{position:absolute;border:1px solid var(--frame);border-radius:6px;background:#fff;overflow:hidden}
.panel-title{height:37px;background:linear-gradient(#17b2ee,#0a9bdc);color:#fff;font-size:20px;line-height:36px;padding-left:21px}
.grid-head{position:absolute;background:var(--head-gray);font-size:14px;line-height:17px;color:var(--ink);display:grid;padding-top:7px}
.grid-rule{position:absolute;height:2px;background:var(--sky-line)}
.grid-body{position:absolute}
.grid-row{display:grid;height:22.5px;align-items:center;font-size:12px;color:var(--ink-soft)}
.grid-row:nth-child(odd){background:var(--row-a)}
.grid-row:nth-child(even){background:var(--row-b)}
.grid-row .ref{color:var(--link)}
.grid-row .doc{color:var(--link);text-decoration:underline}
.cell-pad{padding-left:9px}

.pager{position:absolute;display:flex;align-items:center;gap:2px}
.pager span{width:16px;height:15px;background:var(--sky);color:#fff;font-size:12px;font-weight:700;line-height:15px;text-align:center}
.pager span.is-current{background:var(--navy)}

.dot{display:inline-block;width:13px;height:13px;border-radius:50%;vertical-align:middle}
.dot.red{background:radial-gradient(circle at 40% 35%,#ff9a9a,#e23030)}
.dot.amber{background:radial-gradient(circle at 40% 35%,#fff2a0,#f2c21a)}

.new-request{position:absolute;left:612px;top:843px;width:458px;height:53px;border-radius:6px;
  background:linear-gradient(var(--navy-2),var(--navy));color:#fff;font-size:20px;display:flex;align-items:center;justify-content:center;border:1px solid var(--frame)}

.site-footer{position:absolute;left:89px;top:1114px;width:1024px;height:56px;background:var(--navy);color:#d8d8ee;font-size:14px;line-height:56px;padding-left:50px}
</style>
</head>
<body>

<div class="top-rule"></div>

<div class="brand">
  <div class="brand-dot"></div>
  <div class="brand-name">NORTHVALE PETROCHEMICAL<br>Clearway Desk</div>
</div>

<nav class="main-nav">
  <div class="nav-tab is-active">Home</div>
  <div class="nav-tab is-open">Permits</div>
  <div class="nav-tab">Search</div>
  <div class="nav-tab">Report</div>
  <div class="nav-tab">Admin</div>
  <div class="nav-tab">Help</div>
</nav>

<div class="banner" role="img" aria-label="Petrochemical refinery plant with towers and storage tanks under a cloudy blue sky"></div>
<div class="banner-base"></div>
<div class="nav-rule"></div>

<div class="dropdown">
  <a href="#">Creat New Permit</a>
  <a href="#">Transfer Role</a>
  <a href="#">Transfer Res. Person</a>
</div>

<div class="banner-arrow prev"><svg width="16" height="26" viewBox="0 0 16 26"><path d="M13 2 L3 13 L13 24" fill="none" stroke="#fff" stroke-width="3"/></svg></div>
<div class="banner-arrow next"><svg width="16" height="26" viewBox="0 0 16 26"><path d="M3 2 L13 13 L3 24" fill="none" stroke="#fff" stroke-width="3"/></svg></div>

<!-- New Requests -->
<section class="panel" style="left:135px;top:393px;width:457px;height:229px">
  <div class="panel-title">New Requests</div>
  <div class="grid-head cell-pad" style="left:17px;top:42px;width:419px;height:47px;grid-template-columns:98px 121px 1fr">
    <div>Request<br>No.</div><div>Requested<br>Date</div><div>Branch</div>
  </div>
  <div class="grid-rule" style="left:17px;top:97px;width:419px"></div>
  <div class="grid-body" style="left:17px;top:110px;width:419px">
    <div class="grid-row cell-pad" style="grid-template-columns:98px 121px 1fr"><div class="ref">56-0003</div><div>20/04/2013</div><div>GC1</div></div>
    <div class="grid-row cell-pad" style="grid-template-columns:98px 121px 1fr"><div class="ref">56-0004</div><div>21/04/2013</div><div>GC2</div></div>
  </div>
  <div class="pager" style="left:18px;top:205px">
    <svg width="12" height="16" viewBox="0 0 12 16"><path d="M10 1 L3 8 L10 15" fill="none" stroke="#777" stroke-width="3"/></svg>
    <span class="is-current">1</span><span>2</span><span>3</span><span>4</span>
    <svg width="12" height="16" viewBox="0 0 12 16"><path d="M2 1 L9 8 L2 15" fill="none" stroke="#777" stroke-width="3"/></svg>
  </div>
</section>

<!-- My Working requests -->
<section class="panel" style="left:611px;top:393px;width:458px;height:229px">
  <div class="panel-title" style="padding-left:16px">My Working requests</div>
  <div class="grid-head cell-pad" style="left:18px;top:42px;width:419px;height:47px;grid-template-columns:98px 121px 1fr">
    <div>Request<br>No.</div><div>Requested<br>Date</div><div>Status</div>
  </div>
  <div class="grid-rule" style="left:18px;top:97px;width:421px"></div>
  <div class="grid-body" style="left:18px;top:107px;width:421px">
    <div class="grid-row cell-pad" style="height:23px;grid-template-columns:98px 121px 1fr"><div class="ref">55-0200</div><div>25/03/2013</div><div>Waiting for Process</div></div>
    <div class="grid-row cell-pad" style="height:23px;grid-template-columns:98px 121px 1fr"><div class="ref">55-0210</div><div>24/02/2013</div><div>In Progress</div></div>
    <div class="grid-row cell-pad" style="height:23px;grid-template-columns:98px 121px 1fr"><div class="ref">55-0200</div><div>25/03/2013</div><div>Incomlete Document</div></div>
    <div class="grid-row cell-pad" style="height:23px;grid-template-columns:98px 121px 1fr"><div class="ref">55-0210</div><div>24/02/2013</div><div>Cancel Requested</div></div>
  </div>
  <div class="pager" style="left:19px;top:205px">
    <svg width="12" height="16" viewBox="0 0 12 16"><path d="M10 1 L3 8 L10 15" fill="none" stroke="#777" stroke-width="3"/></svg>
    <span class="is-current">1</span><span>2</span><span>3</span><span>4</span>
    <svg width="12" height="16" viewBox="0 0 12 16"><path d="M2 1 L9 8 L2 15" fill="none" stroke="#777" stroke-width="3"/></svg>
  </div>
</section>

<!-- Expiring Permits -->
<section class="panel" style="left:135px;top:642px;width:934px;height:172px">
  <div class="panel-title" style="padding-left:27px">Expiring Permits</div>
  <div class="grid-head cell-pad" style="left:17px;top:43px;width:893px;height:33px;grid-template-columns:138px 131px 193px 115px 222px 1fr">
    <div>Request No.</div><div>Expiry Date</div><div>Permit Name</div><div>Branch</div><div>Required Time in Days</div><div>Due Date</div>
  </div>
  <div class="grid-rule" style="left:17px;top:76px;width:895px"></div>
  <div class="grid-body" style="left:17px;top:87px;width:895px">
    <div class="grid-row cell-pad" style="grid-template-columns:138px 131px 193px 115px 222px 1fr"><div class="ref">56-0003</div><div>20/04/2013</div><div><span class="doc">Permit Name ###10</span></div><div>GC1</div><div style="padding-left:45px">30&nbsp;&nbsp;&nbsp;&nbsp;<span class="dot red"></span></div><div style="padding-left:3px">-40</div></div>
    <div class="grid-row cell-pad" style="grid-template-columns:138px 131px 193px 115px 222px 1fr"><div class="ref">56-0004</div><div>21/04/2013</div><div><span class="doc">Permit Name ###20</span></div><div>GC2</div><div style="padding-left:45px">60&nbsp;&nbsp;&nbsp;&nbsp;<span class="dot amber"></span></div><div style="padding-left:6px">15</div></div>
  </div>
  <div class="pager" style="left:16px;top:144px">
    <svg width="12" height="16" viewBox="0 0 12 16"><path d="M10 1 L3 8 L10 15" fill="none" stroke="#777" stroke-width="3"/></svg>
    <span class="is-current">1</span><span>2</span><span>3</span><span>4</span>
    <svg width="12" height="16" viewBox="0 0 12 16"><path d="M2 1 L9 8 L2 15" fill="none" stroke="#777" stroke-width="3"/></svg>
  </div>
</section>

<!-- My In Progress Requests -->
<section class="panel" style="left:135px;top:843px;width:458px;height:259px">
  <div class="panel-title" style="padding-left:11px">My In Progress Requests</div>
  <div class="grid-head cell-pad" style="left:19px;top:43px;width:420px;height:47px;grid-template-columns:177px 1fr">
    <div>Request<br>No.</div><div>Requested<br>Date</div>
  </div>
  <div class="grid-rule" style="left:19px;top:97px;width:420px"></div>
  <div class="grid-body" style="left:19px;top:108px;width:420px">
    <div class="grid-row cell-pad" style="height:23px;grid-template-columns:178px 1fr"><div class="ref">55-0200</div><div>25/03/2013</div></div>
    <div class="grid-row cell-pad" style="height:23px;grid-template-columns:178px 1fr"><div class="ref">55-0210</div><div>24/02/2013</div></div>
    <div class="grid-row cell-pad" style="height:23px;grid-template-columns:178px 1fr"><div class="ref">55-0200</div><div>25/03/2013</div></div>
    <div class="grid-row cell-pad" style="height:23px;grid-template-columns:178px 1fr"><div class="ref">55-0200</div><div>25/03/2013</div></div>
    <div class="grid-row cell-pad" style="height:23px;grid-template-columns:178px 1fr"><div class="ref">55-0210</div><div>24/02/2013</div></div>
  </div>
  <div class="pager" style="left:20px;top:233px">
    <svg width="12" height="16" viewBox="0 0 12 16"><path d="M10 1 L3 8 L10 15" fill="none" stroke="#777" stroke-width="3"/></svg>
    <span class="is-current">1</span><span>2</span><span>3</span><span>4</span>
    <svg width="12" height="16" viewBox="0 0 12 16"><path d="M2 1 L9 8 L2 15" fill="none" stroke="#777" stroke-width="3"/></svg>
  </div>
</section>

<div class="new-request">New Request</div>

<!-- Recent Completed Requests -->
<section class="panel" style="left:612px;top:906px;width:458px;height:196px">
  <div class="panel-title" style="padding-left:22px">Recent Completed Requests</div>
  <div class="grid-head cell-pad" style="left:18px;top:43px;width:419px;height:46px;grid-template-columns:96px 123px 1fr">
    <div>Request<br>No.</div><div>Completed<br>Date</div><div>Status</div>
  </div>
  <div class="grid-rule" style="left:18px;top:96px;width:420px"></div>
  <div class="grid-body" style="left:18px;top:109px;width:420px">
    <div class="grid-row cell-pad" style="grid-template-columns:98px 121px 1fr"><div class="ref">56-0003</div><div>20/04/2013</div><div>asdfd jklp fdsa plkj</div></div>
    <div class="grid-row cell-pad" style="grid-template-columns:98px 121px 1fr"><div class="ref">56-0004</div><div>21/04/2013</div><div>asdfd jklp fdsa plkj</div></div>
  </div>
  <div class="pager" style="left:17px;top:170px">
    <svg width="12" height="16" viewBox="0 0 12 16"><path d="M10 1 L3 8 L10 15" fill="none" stroke="#777" stroke-width="3"/></svg>
    <span class="is-current">1</span><span>2</span><span>3</span><span>4</span>
    <svg width="12" height="16" viewBox="0 0 12 16"><path d="M2 1 L9 8 L2 15" fill="none" stroke="#777" stroke-width="3"/></svg>
  </div>
</section>

<footer class="site-footer">Copyrights 2013&nbsp; |&nbsp; Allrights reserved northvalepetrochemical</footer>

</body>
</html>
```